Bricks in the Wall

We need graphics for a 5x7 or 6x9 post card, single sided for a small speech language pathology practice that serves pediatric patients primarily with children on the autism spectrum.

I want a brick wall, with words and phrases written into the bricks. (to follow)
A child standing on top of the wall with hands up in success.
A few incomplete autism puzzles on the ground.
A larger complete autism puzzle in the the child's hand.
The title is: Speech/Language Therapy
The Foundation for Communication Success
Words/phrases to go into the red bricks:
Receptive Language, Expressive Language, Pragmatics, Sensory, cognitive,
social language, autism, articulation, TeleTherapy, auditory processing, screening, evaluation, developmental delay, Goals, family involvement, environmental communication, ASD, Mirror Neurons.
Updates

Target Market(s)

Children with speech and language disorders.

Industry/Entity Type

Speech and Language Therapy

Font styles to use
Serif

Requirements
Must have
• Colors, primary and red bricks.
Nice to have
• I want the postcard to have a happy feel to it and a sense of success.
Should not have
• I don't want it cluttered.

```html
<!DOCTYPE html>
<html lang="en">
<head>
<meta charset="utf-8">
<title>Speech/Language Therapy – The Foundation for Communication Success</title>
<link rel="stylesheet" href="https://fonts.googleapis.com/css2?family=Merriweather:wght@700;900&display=swap">
<style>
  :root {
    --wall-light: #ececec;
    --wall-mid: #d2d2d2;
    --wall-dark: #9a9a9a;
    --banner-red: #d8131b;
    --banner-dark: #b00d14;
    --brick-yellow: #fcc419;
    --brick-yellow-edge: #e2a800;
    --brick-brown: #a3410b;
    --brick-brown-edge: #7d2f06;
    --ink-brown: #4a1a02;
    --ink-white: #ffffff;
    --base-brick: #9c3a22;
    --mortar: #6f6f6f;
    --gravel: #a9a49c;
    --paving: #c9b7ad;
    --paving-joint: #a99a92;
    --scene-light: #e3d6c8;
    --scene-dark: #9a938c;
  }
  * { margin: 0; padding: 0; box-sizing: border-box; }
  html, body { width: 1200px; height: 800px; overflow: hidden; background: #fff; }
  .canvas {
    position: relative;
    width: 1200px;
    height: 800px;
    overflow: hidden;
    font-family: "Merriweather", Georgia, serif;
    background: radial-gradient(ellipse at 50% 45%, var(--wall-light) 0%, var(--wall-mid) 60%, var(--wall-dark) 100%);
  }
  .top-strip {
    position: absolute; left: 0; top: 0; width: 1200px; height: 28px;
    background: linear-gradient(#8d8d8d, #b4b4b4);
  }
  .title-banner {
    position: absolute; left: 0; top: 28px; width: 1200px; height: 100px;
    background: linear-gradient(var(--banner-red), var(--banner-dark));
    display: flex; flex-direction: column; align-items: center; justify-content: center;
    color: var(--ink-white);
    text-shadow: 2px 2px 3px rgba(0,0,0,0.45);
    white-space: nowrap;
  }
  .title-banner h1 {
    font-weight: 900;
    font-size: 42px;
    line-height: 1.15;
  }
  .title-banner .subtitle {
    font-weight: 700;
    font-size: 24px;
    line-height: 1.3;
  }
  .child-photo {
    position: absolute; left: 245px; top: 128px; width: 210px; height: 662px;
    background: linear-gradient(180deg, var(--scene-light), var(--scene-dark));
  }
  .brick {
    position: absolute;
    display: flex; align-items: center; justify-content: center;
    font-weight: 700;
    font-size: 30px;
    letter-spacing: -0.5px;
    white-space: nowrap;
    height: 87px;
    border: 1px solid rgba(0,0,0,0.25);
    box-shadow: inset 0 0 0 2px rgba(255,255,255,0.12), 1px 2px 3px rgba(0,0,0,0.25);
  }
  .brick--yellow {
    background: linear-gradient(var(--brick-yellow), var(--brick-yellow-edge));
    color: var(--ink-brown);
  }
  .brick--brown {
    background: linear-gradient(var(--brick-brown), var(--brick-brown-edge));
    color: var(--ink-white);
    text-shadow: 1px 1px 2px rgba(0,0,0,0.5);
  }
  .brick--text-right { justify-content: flex-end; padding-right: 14px; }
  .base-course {
    position: absolute; left: 0; top: 682px; width: 1200px; height: 26px;
    background: repeating-linear-gradient(90deg, var(--base-brick) 0 60px, var(--mortar) 60px 63px);
  }
  .gravel {
    position: absolute; left: 0; top: 706px; width: 1200px; height: 36px;
    background: var(--gravel);
  }
  .paving {
    position: absolute; left: 0; top: 742px; width: 1200px; height: 58px;
    background: repeating-linear-gradient(90deg, var(--paving) 0 150px, var(--paving-joint) 150px 152px);
  }
</style>
</head>
<body>
<main class="canvas">
  <div class="top-strip"></div>
  <header class="title-banner">
    <h1>Speech/Language Therapy</h1>
    <p class="subtitle">The Foundation for Communication Success</p>
  </header>

  <section class="wall">
    <div class="brick brick--yellow" style="left:63px;top:175px;width:167px;">Autism</div>
    <div class="brick brick--yellow" style="left:506px;top:175px;width:187px;">ASD</div>
    <div class="brick brick--brown" style="left:714px;top:175px;width:240px;">Pragmatics</div>
    <div class="brick brick--yellow" style="left:971px;top:175px;width:188px;">Cognitive</div>

    <div class="brick brick--yellow" style="left:30px;top:279px;width:188px;"></div>
    <div class="brick brick--yellow" style="left:481px;top:279px;width:187px;">Screening</div>
    <div class="brick brick--brown" style="left:686px;top:279px;width:188px;"></div>
    <div class="brick brick--yellow" style="left:890px;top:279px;width:247px;">Articulation</div>

    <div class="brick brick--yellow" style="left:66px;top:383px;width:166px;"></div>
    <div class="brick brick--yellow" style="left:475px;top:383px;width:188px;"></div>
    <div class="brick brick--brown" style="left:680px;top:383px;width:278px;">Evaluation</div>
    <div class="brick brick--yellow" style="left:975px;top:383px;width:188px;">Goals</div>

    <div class="brick brick--yellow" style="left:28px;top:486px;width:189px;">Sensory</div>
    <div class="brick brick--yellow brick--text-right" style="left:440px;top:486px;width:248px;">TeleTherapy</div>
    <div class="brick brick--brown" style="left:705px;top:486px;width:92px;"></div>
    <div class="brick brick--yellow" style="left:812px;top:486px;width:350px;">Social Language</div>

    <div class="brick brick--yellow" style="left:-10px;top:585px;width:150px;"></div>
    <div class="brick brick--brown" style="left:157px;top:585px;width:183px;"></div>
    <div class="brick brick--yellow" style="left:360px;top:585px;width:188px;"></div>
    <div class="brick brick--brown" style="left:565px;top:585px;width:188px;"></div>
    <div class="brick brick--yellow" style="left:770px;top:585px;width:188px;"></div>
    <div class="brick brick--brown" style="left:975px;top:585px;width:187px;"></div>
    <div class="brick brick--yellow" style="left:1180px;top:585px;width:40px;"></div>
  </section>

  <div class="base-course"></div>
  <div class="gravel"></div>
  <div class="paving"></div>

  <div class="child-photo" role="img" aria-label="Photo of a young child in a striped shirt climbing a grey ladder leaning against the brick wall, reaching for the top"></div>
</main>
</body>
</html>
```